Roaming Kestrel (hail repair) Company seeks Web design

We are looking for someone to design a website for an automotive hail damage repair business. We are a national company that travels to cities that have suffered a catastrophic hail event, where we set up for retail customers to come in and have all of their auto hail repair needs handled.
We had a website in the past, but due to a technical error it has been deleted. You can view the old webpage by going to old.pagevault.net and searching www.Pellet-Yard.com and looking under the date June 3rd 2015. We are hoping to have something similar to the original, but more extensive and updated. We would also like to add a page that allows our customers to get an online estimate by filling in their own damage assessment. There is a great example of what we are looking for if you go to www.smoothcoatworkshop.com and click on "Get An Estimate".

Target Market(s)

USA

Industry/Entity Type

Automotive

Number of Pages Required

5+ page

Requirements
Must have
• Mobile Friendly, easy for me to change locations on the location page along with the map. A link to google maps app from site.

```html
<!DOCTYPE html>
<html lang="en">
<head>
<meta charset="utf-8">
<title>Pellet Yard — Auto Hail Repair</title>
<link href="https://fonts.googleapis.com/css2?family=Roboto:wght@400;500;700&family=Open+Sans:ital,wght@0,400;0,600;0,700;1,400&display=swap" rel="stylesheet">
<style>
:root{
  --yellow:#e2bd10;
  --yellow-dark:#c9a40a;
  --ink:#1d1d1d;
  --text:#555;
  --muted:#777;
  --page:#ececec;
  --panel:#f7f7f7;
  --line:#dcdcdc;
  --footer:#222;
  --footer-text:#e8e8e8;
}
*{box-sizing:border-box;margin:0;padding:0}
html,body{width:817px;height:1200px;overflow:hidden}
body{position:relative;background:linear-gradient(180deg,#f4f4f4 0,#e9e9e9 100%);font-family:"Open Sans",sans-serif;color:var(--text)}
.abs{position:absolute}
.top-rule{left:0;top:0;width:817px;height:3px;background:var(--yellow)}
.header-curve{left:0;top:60px}
.brand{left:67px;top:26px;font-family:"Roboto",sans-serif;font-weight:700;font-size:25px;color:var(--yellow);letter-spacing:.5px;display:flex;align-items:center;gap:8px}
.brand .mark{width:12px;height:12px;background:var(--yellow)}
.contact-strip{right:68px;top:13px;display:flex;gap:16px;font-family:"Roboto",sans-serif;font-size:11px;color:#444;align-items:center}
.contact-strip .phone{font-size:13px;font-weight:500}
.contact-strip span{display:flex;align-items:center;gap:7px}
.nav{left:324px;top:44px;display:flex;gap:17px;font-family:"Roboto",sans-serif;font-size:9.5px;font-weight:500;color:#333;letter-spacing:.2px}
.nav .active{color:var(--yellow)}
.nav-search{left:736px;top:43px}
.panel{left:67px;top:95px;width:683px;height:900px;background:var(--panel)}
.tabs{left:85px;top:95px;width:648px;height:35px;display:flex;background:var(--yellow)}
.tabs div{flex:1;display:flex;align-items:center;justify-content:center;gap:6px;font-family:"Roboto",sans-serif;font-size:11px;font-weight:500;color:#fff;border-right:1px solid rgba(255,255,255,.25)}
.tabs div:last-child{border:none}
.hero{left:85px;top:130px;width:648px;height:275px;background:linear-gradient(120deg,#d9d5cc 0%,#c8c3b8 40%,#7b7e82 70%,#9a9a98 100%)}
.hero-band{left:197px;top:237px;width:424px;height:62px;background:rgba(255,255,255,.55)}
.hero-title{left:85px;top:254px;width:648px;text-align:center;font-family:"Roboto",sans-serif;font-weight:700;font-size:24px;color:var(--ink);letter-spacing:.2px}
.hero-title em{font-style:normal;color:var(--yellow)}
.dots{left:381px;top:366px;display:flex;gap:2px}
.dots i{width:12px;height:12px;border-radius:50%;border:1.5px solid #fff;display:block}
.dots i.on{background:var(--yellow);border-color:#fff}
.feature{top:425px;width:180px;height:93px;background:linear-gradient(180deg,#fff,#ececec);border:1px solid var(--line);padding:12px 10px 0 44px}
.feature h3{font-family:"Roboto",sans-serif;font-size:11px;font-weight:500;color:var(--ink);margin-bottom:8px}
.feature p{font-size:7.6px;line-height:16.5px;color:var(--muted)}
.feature p b{font-weight:400;color:var(--yellow)}
.feature .more{font-size:7.5px;font-weight:700;color:var(--yellow);margin-top:3px}
.badge-icon{top:443px;width:56px;height:56px;border-radius:50%;background:var(--yellow);border:3px solid #fff;box-shadow:0 0 0 1px #ddd;display:flex;align-items:center;justify-content:center}
.divider{left:85px;width:648px;height:1px;background:var(--line)}
.section-title{font-family:"Roboto",sans-serif;font-weight:500;font-size:15.5px;color:var(--ink);display:flex;align-items:center;gap:4px}
.welcome-title{left:85px;top:568px}
.seal{left:90px;top:610px;width:106px;height:106px;border-radius:50%;background:radial-gradient(circle,#e2bd10 0 55%,#2a2a2a 56% 100%)}
.body-copy{font-size:7.8px;line-height:18px;color:var(--text)}
.welcome-copy-a{left:228px;top:617px;width:230px}
.welcome-copy-b{left:84px;top:720px;width:380px}
.read-more{font-size:7.5px;font-weight:700;color:var(--yellow)}
.video{left:473px;top:585px;width:258px;height:188px;border:3px solid #fff;box-shadow:0 0 0 1px #ddd;background:linear-gradient(135deg,#c9ccd0 0%,#6b7078 45%,#2f3238 75%,#8a8d92 100%)}
.contact-title{left:0;top:831px;width:817px;justify-content:center}
.contact-copy{left:0;top:862px;width:817px;text-align:center;font-style:italic;font-size:9.3px;line-height:16px;color:var(--muted)}
.btn{background:var(--yellow);color:#fff;font-family:"Roboto",sans-serif;font-weight:500;display:flex;align-items:center;justify-content:center;border-bottom:2px solid var(--yellow-dark)}
.quote-btn{left:341px;top:910px;width:136px;height:35px;font-size:11.5px}
.footer-shape{left:0;top:920px}
.footer-brand{left:67px;top:1051px;font-family:"Roboto",sans-serif;font-weight:700;font-size:22px;color:#fff;display:flex;align-items:center;gap:8px}
.footer-brand .mark{width:11px;height:11px;background:#fff}
.col-rule{top:1010px;width:1px;height:125px;background:#333}
.footer h4{font-family:"Roboto",sans-serif;font-weight:500;font-size:10.5px;color:#fff;letter-spacing:.2px}
.f-info{left:274px;top:1016px}
.f-info ul{list-style:none;margin-top:14px}
.f-info li{font-size:7.8px;line-height:13.6px;color:var(--footer-text)}
.f-news{left:395px;top:1016px;width:180px}
.f-news p{font-size:7.8px;line-height:14px;color:var(--footer-text);margin-top:14px}
.email-field{left:395px;top:1075px;width:179px;height:24px;background:#fff;font-size:7.8px;color:#777;padding:7px 10px}
.subscribe{left:395px;top:1107px;width:68px;height:25px;font-size:9.5px;font-weight:700}
.f-contact{left:620px;top:1016px}
.f-contact ul{list-style:none;margin-top:14px}
.f-contact li{display:flex;gap:10px;font-size:7.8px;line-height:10.5px;color:var(--footer-text);margin-bottom:10px;align-items:flex-start}
.f-contact li:first-child{margin-bottom:14px}
.bottom-rule{left:67px;top:1153px;width:683px;height:1px;background:#2e2e2e}
.copyright{left:67px;top:1173px;font-size:7.8px;color:#fff}
.social{left:637px;top:1166px;display:flex;gap:3px}
.social i{display:block;width:26px;height:26px;border-radius:50%;border:1.5px solid #ddd}
</style>
</head>
<body>
<div class="abs top-rule"></div>
<svg class="abs header-curve" width="817" height="60" viewBox="0 0 817 60" aria-hidden="true">
  <path d="M0 50 Q408 10 817 42 L817 48 Q408 18 0 58 Z" fill="#dcdcdc"/>
</svg>

<div class="abs brand"><span>PELLET YARD</span><span class="mark"></span></div>

<div class="abs contact-strip">
  <span><svg width="13" height="9" viewBox="0 0 13 9"><rect width="13" height="9" fill="#e2bd10"/><path d="M0 0 L6.5 5 L13 0" stroke="#fff" fill="none"/></svg>hello@pelletyard.com</span>
  <span class="phone"><svg width="10" height="10" viewBox="0 0 10 10"><path d="M2 0 L4 2.5 L3 4 Q4.5 6 6 7 L7.5 6 L10 8 L8.5 10 Q2 9 0 1.5 Z" fill="#e2bd10"/></svg>866-555-0142</span>
</div>

<nav class="abs nav">
  <span class="active">HOME</span><span>ABOUT US »</span><span>WHAT IS PDR?</span><span>SERVICES</span><span>GALLERY</span><span>NEWS</span><span>CONTACT</span>
</nav>
<svg class="abs nav-search" width="11" height="11" viewBox="0 0 11 11" aria-label="Search"><circle cx="4.5" cy="4.5" r="3.3" stroke="#333" stroke-width="1.6" fill="none"/><path d="M7 7 L10.2 10.2" stroke="#333" stroke-width="1.8"/></svg>

<div class="abs panel"></div>

<div class="abs tabs">
  <div><svg width="8" height="10" viewBox="0 0 8 10"><rect x=".5" y=".5" width="7" height="9" stroke="#fff" fill="none"/><path d="M2 3.5H6M2 5.5H6M2 7.5H6" stroke="#fff"/></svg>GET AN ESTIMATE</div>
  <div><svg width="7" height="10" viewBox="0 0 7 10"><path d="M3.5 10 L0.5 4.5 A3 3 0 1 1 6.5 4.5 Z" fill="#fff"/><circle cx="3.5" cy="3.5" r="1.2" fill="#e2bd10"/></svg>FIND A LOCATION</div>
  <div><svg width="8" height="10" viewBox="0 0 8 10"><rect x=".5" y=".5" width="7" height="9" stroke="#fff" fill="none"/><path d="M2 3.5H6M2 5.5H6M2 7.5H6" stroke="#fff"/></svg>SCHEDULE AN APPOINTMENT</div>
</div>

<div class="abs hero" role="img" aria-label="Smiling customer holding car keys while sitting on the bonnet of a dark sedan"></div>
<div class="abs hero-band"></div>
<h1 class="abs hero-title">FREE <em>LOANER</em> CARS <em>AVAILABLE</em></h1>
<div class="abs dots"><i class="on"></i><i></i><i></i><i></i></div>

<div class="abs feature" style="left:109px">
  <h3>Easy &amp; Reliable Service</h3>
  <p>We want to make this process as easy for you as possible.</p>
  <div class="more">READ MORE &gt;&gt;</div>
</div>
<div class="abs badge-icon" style="left:85px">
  <svg width="30" height="20" viewBox="0 0 30 20"><path d="M3 14 L5 8 Q6 5 9 5 L19 5 Q22 5 24 8 L27 10 Q29 11 29 14 Z" fill="#fff"/><circle cx="9" cy="15" r="3" fill="#fff" stroke="#e2bd10" stroke-width="1.5"/><circle cx="22" cy="15" r="3" fill="#fff" stroke="#e2bd10" stroke-width="1.5"/></svg>
</div>

<div class="abs feature" style="left:331px">
  <h3>How Easy?</h3>
  <p><b>Step 1:</b> &nbsp;Contact Us<br><b>Step 2:</b> &nbsp;Drop your car off<br><b>Step 3:</b> &nbsp;Pick your car up</p>
</div>
<div class="abs badge-icon" style="left:307px">
  <svg width="32" height="32" viewBox="0 0 32 32"><circle cx="16" cy="16" r="13" stroke="#fff" stroke-width="2.5" fill="none"/><circle cx="16" cy="16" r="6" stroke="#fff" stroke-width="3" fill="none" stroke-dasharray="4 2.3"/><circle cx="16" cy="16" r="2" fill="#fff"/></svg>
</div>

<div class="abs feature" style="left:553px">
  <h3>Lifetime Guarantee</h3>
  <p>That's correct, we offer a full written lifetime guarantee to all ..</p>
  <div class="more">READ MORE &gt;&gt;</div>
</div>
<div class="abs badge-icon" style="left:529px">
  <svg width="32" height="32" viewBox="0 0 32 32"><circle cx="16" cy="16" r="12" stroke="#fff" stroke-width="3" fill="none"/><path d="M10 16 L14.5 20.5 L22 12" stroke="#fff" stroke-width="3.2" fill="none"/></svg>
</div>

<div class="abs divider" style="top:545px"></div>

<h2 class="abs section-title welcome-title">WELCOME TO <span style="display:inline-block;width:8px;height:8px;background:var(--yellow);margin:0 2px"></span> PELLET YARD</h2>

<div class="abs seal" role="img" aria-label="Quality guarantee seal"></div>

<div class="abs body-copy welcome-copy-a">Our mission is to provide you with a stress-free experience while taking care of all of your needs in an efficient and professional manner.<br>We want to make this process as easy for you as possible. Pellet Yard is dedicated to making that a reality. We work</div>
<div class="abs welcome-copy-b">
  <p class="body-copy">with all major insurance carriers, and we have knowledgeable staff that will work directly with your insurance company to ensure your experience is hassle-free.</p>
  <p class="read-more" style="margin-top:10px">READ MORE &gt;&gt;</p>
</div>

<div class="abs video" role="img" aria-label="Video: two mechanics working under the open hood of a car">
  <svg style="position:absolute;left:117px;top:79px" width="24" height="24" viewBox="0 0 24 24"><circle cx="12" cy="12" r="12" fill="rgba(0,0,0,.35)"/><path d="M9 6 L18 12 L9 18 Z" fill="#fff"/></svg>
</div>

<div class="abs divider" style="top:801px"></div>

<h2 class="abs section-title contact-title">CONTACT US <span style="display:inline-block;width:8px;height:8px;background:var(--yellow);margin:0 3px"></span> TODAY FOR FREE QUOTE</h2>
<p class="abs contact-copy">Please contact us for a free quote or if you need further assistance. Use the interactive<br>map below for information on how to get to our locations.</p>

<svg class="abs footer-shape" width="817" height="280" viewBox="0 0 817 280" aria-hidden="true">
  <path d="M0 10 Q408 95 817 10 L817 280 L0 280 Z" fill="#e2bd10"/>
  <path d="M0 30 Q408 138 817 22 L817 280 L0 280 Z" fill="#222"/>
</svg>

<div class="abs btn quote-btn">GET A FREE QUOTE</div>

<footer class="footer">
  <div class="abs footer-brand"><span>PELLET YARD</span><span class="mark"></span></div>
  <div class="abs col-rule" style="left:250px"></div>
  <div class="abs col-rule" style="left:368px"></div>
  <div class="abs col-rule" style="left:598px"></div>

  <div class="abs f-info">
    <h4>INFORMATION</h4>
    <ul><li>Home</li><li>About us</li><li>what is PDR?</li><li>Services</li><li>Gallery</li><li>News</li><li>Contact</li></ul>
  </div>

  <div class="abs f-news">
    <h4>NEWSLETTER</h4>
    <p>Register Your email address to get information about us</p>
  </div>
  <div class="abs email-field">Email Address</div>
  <div class="abs btn subscribe">SUBSCRIBE</div>

  <div class="abs f-contact">
    <h4>CONTACT US</h4>
    <ul>
      <li><svg width="7" height="10" viewBox="0 0 7 10"><path d="M3.5 10 L0.5 4.5 A3 3 0 1 1 6.5 4.5 Z" fill="#fff"/><circle cx="3.5" cy="3.5" r="1.2" fill="#222"/></svg><span>Pellet-Yard , 2180 S Ridge Rd<br>Marlow, Tx</span></li>
      <li><svg width="9" height="9" viewBox="0 0 10 10"><path d="M2 0 L4 2.5 L3 4 Q4.5 6 6 7 L7.5 6 L10 8 L8.5 10 Q2 9 0 1.5 Z" fill="#fff"/></svg><span>866-555-0142</span></li>
      <li><svg width="10" height="9" viewBox="0 0 10 9"><rect x="0" y="2" width="10" height="7" fill="#fff"/><rect x="2" y="0" width="6" height="3" fill="#fff"/><rect x="2" y="4" width="6" height="1" fill="#222"/></svg><span>877-555-0198</span></li>
      <li><svg width="10" height="7" viewBox="0 0 13 9"><rect width="13" height="9" fill="#fff"/><path d="M0 0 L6.5 5 L13 0" stroke="#222" fill="none"/></svg><span>hello@pelletyard.com</span></li>
    </ul>
  </div>

  <div class="abs bottom-rule"></div>
  <p class="abs copyright">Copyright © 2016, Pellet- Yard . All Rights Reserved ,</p>
  <div class="abs social" aria-label="Social links"><i></i><i></i><i></i><i></i></div>
</footer>
</body>
</html>
```